Brell Harbor Company Business Cards

Front and Back Business Card - logo and text setup - cool design. I need workable photoshop or illustrator files so I can setup each employee card with design that is created
Updates

Hi everyone, thank you for the great entries. Please no more white and blue cards - there are so many already - black and silver only now please. thanks!

Target Market(s)

Construction Industry - Facility Managers

Industry/Entity Type

Construction

Contact Information for Business Card

I really like contemporary simplistic looks - clean neat....not opposed to seeing some black backrounds

Requirements
Must have
• Logo/website address with design on front only - www.brellharbor-example.com (logo attached)
• Back:
• Name/Title/Company Address/Phone/email address
Nice to have
• Cool design
Should not have
• Nothing gimmicky like Fire or Water - since we are a Fire Protection company - it has all been done

```html
<!DOCTYPE html>
<html lang="en">
<head>
<meta charset="utf-8">
<title>Brell Harbor Company Business Cards</title>
<link rel="stylesheet" href="https://fonts.googleapis.com/css2?family=Roboto:ital,wght@0,400;0,500;0,700;1,500&display=swap">
<style>
  :root {
    --black: #141516;
    --charcoal: #2a2c2f;
    --silver: #b9bdc2;
    --silver-light: #e4e6e8;
    --silver-pale: #f3f4f5;
    --ink: #1c1d1f;
    --ink-soft: #4a4d52;
    --backdrop: #e6e2dc;
    --rule: #8a8e93;
  }
  * { margin: 0; padding: 0; box-sizing: border-box; }
  html, body { width: 900px; height: 1200px; overflow: hidden; }
  body {
    background: var(--backdrop);
    font-family: "Roboto", Arial, sans-serif;
    color: var(--ink);
    position: relative;
  }
  .card {
    position: absolute;
    left: 85px;
    width: 733px;
    height: 428px;
    border-radius: 24px;
    overflow: hidden;
  }

  /* Front: logo and website only */
  .card-front {
    top: 138px;
    background: linear-gradient(135deg, var(--charcoal) 0%, var(--black) 60%);
  }
  .wordmark {
    position: absolute;
    left: 0;
    width: 100%;
    top: 182px;
    text-align: center;
    font-weight: 700;
    font-size: 60px;
    letter-spacing: -1px;
    line-height: 1;
    color: var(--silver);
  }
  .front-url {
    position: absolute;
    left: 0;
    width: 100%;
    top: 368px;
    text-align: center;
    color: var(--silver-light);
    font-size: 18px;
    font-style: italic;
    font-weight: 500;
  }

  /* Back: name, title, contact details */
  .card-back {
    top: 634px;
    background: linear-gradient(135deg, var(--silver-pale) 0%, var(--silver-pale) 40%, var(--silver-light) 100%);
  }
  .company-name {
    position: absolute;
    left: 52px; top: 78px;
    font-size: 30px;
    font-weight: 700;
    letter-spacing: -0.5px;
    color: var(--black);
  }
  .person { position: absolute; left: 52px; top: 220px; }
  .person-name { color: var(--black); font-size: 24px; font-weight: 500; line-height: 30px; }
  .person-title { font-size: 17px; line-height: 22px; color: var(--ink-soft); }
  .divider {
    position: absolute;
    left: 52px; top: 283px;
    width: 631px; height: 1.5px;
    background: var(--rule);
  }
  .contact-list {
    position: absolute;
    left: 52px; top: 296px;
    list-style: none;
  }
  .contact-list li {
    display: flex; align-items: center;
    font-size: 16px; line-height: 24px;
  }
  .contact-list svg { width: 18px; height: 18px; margin-right: 13px; flex: none; }
  .address {
    position: absolute;
    left: 466px; top: 299px;
    display: flex;
    font-size: 16px; line-height: 22.5px;
    font-style: normal;
  }
  .address svg { width: 18px; height: 22px; margin-right: 13px; margin-top: 1px; flex: none; }
  .accent-bands { position: absolute; left: 0; bottom: 0; width: 733px; height: 22px; }
</style>
</head>
<body>

<section class="card card-front" aria-label="Card front">
  <div class="wordmark">Brell Harbor</div>
  <div class="front-url">www.brellharbor-example.com</div>
</section>

<section class="card card-back" aria-label="Card back">
  <div class="company-name">Brell Harbor Company</div>

  <div class="person">
    <div class="person-name">Dana Whitlock</div>
    <div class="person-title">President</div>
  </div>

  <div class="divider"></div>

  <ul class="contact-list">
    <li>
      <svg viewBox="0 0 24 24" aria-hidden="true"><path fill="#141516" d="M6.6 10.8a15.1 15.1 0 0 0 6.6 6.6l2.2-2.2c.3-.3.7-.4 1-.2 1.1.4 2.3.6 3.6.6.6 0 1 .4 1 1V20c0 .6-.4 1-1 1A17 17 0 0 1 3 4c0-.6.4-1 1-1h3.5c.6 0 1 .4 1 1 0 1.3.2 2.5.6 3.6.1.3 0 .7-.2 1z"/></svg>
      555.014.2290
    </li>
    <li>
      <svg viewBox="0 0 24 24" aria-hidden="true"><rect x="2" y="5" width="20" height="14" rx="1" fill="#141516"/><path d="M2.5 5.5 12 13l9.5-7.5" fill="none" stroke="#f3f4f5" stroke-width="1.6"/></svg>
      info@brellharbor-example.com
    </li>
  </ul>

  <address class="address">
    <svg viewBox="0 0 24 28" aria-hidden="true"><path fill="#141516" d="M12 1a9 9 0 0 0-9 9c0 7 9 17 9 17s9-10 9-17a9 9 0 0 0-9-9z"/><circle cx="12" cy="10" r="3.6" fill="#f3f4f5"/></svg>
    <span>18 Quarry Lane<br>Suite 210, Alder Falls<br>MI 40000</span>
  </address>

  <svg class="accent-bands" viewBox="0 0 733 22" aria-hidden="true">
    <polygon points="0,0 280,0 302,22 0,22" fill="var(--black)"/>
    <polygon points="288,10 733,10 733,22 300,22" fill="var(--silver)"/>
  </svg>
</section>

</body>
</html>
```